Flyer Design Project for our Parenting Psychologists at the Bright Harbour Wellbeing Clinic

At the Bright Harbour Wellbeing Clinic we have expert Parenting Psychologists.

Parenting Psychologists provide practical, step by step assistance to parents who are struggling with their children's behavioural and emotional problems.

We need a DL size brochure that will be appealing to parents. The brochure will be on show in schools, kindergartens and GP clinics.

In terms of style it will be in line with our website and stationery that I will attach.

www.brightharbourwellbeing.com.au
Updates

Hi Everyone,
Thanks for putting forward your proposals, there are a couple there that I am very interested in. I am looking to see if there is a way that I can change my brief to guaranteed as I am definitely going to be using one of the designs for sure.
I have emailed ArtFolkly and as soon as I get an answer I will change it if I can.
If anyone out there already knows the answer please let me know :-)
Thanks,
Marnie.

Hi Again,

I worked it out myself!!

I have now changed this to a committed project.

Kind regards,
Marnie.

Reason: I have 46 designs now and need more time to work out which is best!

Target Market(s)

The target will be educated professional parents motivated to get professional help. And doctors and teachers who will pass on the brochures 2 parents

Industry/Entity Type

Health

Requirements
Must have
• I want one DL size brochure. Back and front.

We need text (below) and our contact details. Our logo.

9362 4158
Suite 4, 2071 Pellbrook Rd, Ferndale Heights 3587

Text:
Parents want the best for their kids. They want kids that are happy, healthy and well behaved.

So why is it so hard? Parents of toddlers, primary schoolers and teenagers alike say that they are frustrated by constant nagging, bribing and yelling, they don't know what to try next. Some parents worry that their children are unhappy. Struggling at school, not making friends or coping with bigger problems.

The good news is that getting your children to behave more co-operatively doesn't need to be difficult or mysterious. We all know that kids don't come with manuals, but there are skills every parent can learn to make parenting easier. In a few sessions with a Parenting Psychologist, you will receive step by step guidance in how to talk to your children in a way that will be much more effective getting them to behave in a respectful and co-operative way around the home and in public. You will learn how to help your child cope with problems they are going through. They can help you reconnect with your kids so you can enjoy being a parent again.

Nice to have
• Themes consistent with our website
and letterhead, business cards. I will attach these.
Should not have
• I don't want it to look too cluttered so if the text I have provided up above looks too crowded then I will edit it.

```html
<!DOCTYPE html>
<html lang="en">
<head>
<meta charset="utf-8">
<title>Bright Harbour Wellbeing Clinic – Parenting Brochure</title>
<link rel="stylesheet" href="https://fonts.googleapis.com/css2?family=Lato:wght@300;400;700&display=swap">
<style>
  :root {
    --teal: #6fb1b7;
    --teal-dark: #5e9fa6;
    --slate: #8797a8;
    --slate-band: #7d9bae;
    --lavender: #c8cce8;
    --paper: #ffffff;
    --panel-grey: #eceeee;
    --ink: #3f4448;
    --brand-grey: #8a8f93;
    --rule: #dcdfe0;
    --bg: #f1f2f2;
    --photo-a: #8fb865;
    --photo-b: #cfa08a;
  }
  * { box-sizing: border-box; margin: 0; padding: 0; }
  html, body { width: 1200px; height: 795px; overflow: hidden; }
  body {
    background: var(--bg);
    font-family: 'Lato', sans-serif;
    color: var(--ink);
    display: flex;
    justify-content: center;
    align-items: center;
    gap: 60px;
  }
  .panel {
    width: 340px;
    height: 730px;
    background: var(--paper);
    display: flex;
    flex-direction: column;
    overflow: hidden;
    box-shadow: 0 2px 8px rgba(0,0,0,0.08);
  }
  .stripe {
    height: 10px;
    flex: none;
    background: linear-gradient(90deg,
      var(--slate) 0 14%, var(--teal) 14% 30%, var(--panel-grey) 30% 44%,
      var(--teal) 44% 62%, var(--slate) 62% 78%, var(--teal) 78% 100%);
  }

  /* Back panel */
  .back .intro {
    padding: 24px 26px 20px;
    color: var(--teal-dark);
    font-size: 16px;
    line-height: 1.3;
    border-bottom: 1px solid var(--rule);
  }
  .back .copy { padding: 18px 26px 0; flex: 1; }
  .back h2 {
    font-size: 13px;
    font-weight: 700;
    letter-spacing: 0.3px;
    margin-bottom: 10px;
  }
  .back .body {
    font-size: 11px;
    line-height: 1.45;
    padding-bottom: 12px;
  }
  .back .body + .body {
    border-top: 1px solid var(--rule);
    padding-top: 12px;
  }
  .back .contact-band {
    flex: none;
    background: var(--slate-band);
    color: #fff;
    text-align: center;
    padding: 18px 20px 16px;
    font-size: 12.5px;
    line-height: 1.6;
  }
  .back .contact-band strong { font-weight: 700; margin-right: 6px; }

  /* Front panel */
  .front { background: var(--panel-grey); }
  .front .headline {
    padding: 30px 26px 20px;
    color: var(--teal);
    font-size: 22px;
    font-weight: 400;
    line-height: 1.2;
  }
  .front .photo {
    height: 250px;
    flex: none;
    background: linear-gradient(160deg, #a9cc84 0%, var(--photo-a) 45%, var(--photo-b) 80%, #9fc173 100%);
  }
  .front .brand {
    display: flex;
    align-items: center;
    gap: 16px;
    padding: 34px 28px 28px;
  }
  .front .brand-mark {
    width: 46px; height: 46px;
    border-radius: 50%;
    background: #fff;
    flex: none;
  }
  .front .brand-name {
    font-size: 15px;
    font-weight: 300;
    letter-spacing: 3px;
    text-transform: uppercase;
    line-height: 1.3;
    color: var(--brand-grey);
  }
  .front .contact-box {
    margin-left: 22px;
    flex: 1;
    background: var(--lavender);
    border-radius: 16px 0 0 16px;
    clip-path: polygon(0 0, 82% 0, 100% 22%, 100% 100%, 0 100%);
    padding: 86px 20px 20px 24px;
    font-size: 13px;
    font-style: normal;
    line-height: 1.45;
    color: var(--ink);
  }
  .front .contact-box strong { font-weight: 700; margin-right: 6px; }
  .front .foot { height: 14px; flex: none; }
</style>
</head>
<body>
  <section class="panel back">
    <div class="stripe"></div>
    <p class="intro">Parents want the best for their kids. They want kids that are happy, healthy and well behaved.</p>
    <div class="copy">
      <h2>SO WHY IS IT SO HARD?</h2>
      <p class="body">Parents of toddlers, primary schoolers and teenagers alike say that they are frustrated by constant nagging, bribing and yelling, they don't know what to try next. Some parents worry that their children are unhappy. Struggling at school, not making friends or coping with bigger problems.</p>
      <p class="body">The good news is that getting your children to behave more co-operatively doesn't need to be difficult or mysterious. We all know that kids don't come with manuals, but there are skills every parent can learn to make parenting easier. In a few sessions with a Parenting Psychologist, you will receive step by step guidance in how to talk to your children in a way that will be much more effective getting them to behave in a respectful and co-operative way around the home and in public. You will learn how to help your child cope with problems they are going through. They can help you reconnect with your kids so you can enjoy being a parent again.</p>
    </div>
    <div class="contact-band">
      <div><strong>tel</strong>9362 4158</div>
      <div>www.brightharbourwellbeing.com.au</div>
    </div>
    <div class="stripe"></div>
  </section>

  <section class="panel front">
    <div class="stripe"></div>
    <h1 class="headline">Expert Parenting Advice.<br>Toddlers to Teens.</h1>
    <div class="photo" role="img" aria-label="Photo of a mother and young child sitting on a picnic rug in a sunny park"></div>
    <div class="stripe"></div>
    <div class="brand">
      <span class="brand-mark"></span>
      <span class="brand-name">Bright Harbour Wellbeing Clinic</span>
    </div>
    <address class="contact-box">
      <div><strong>tel</strong>9362 4158</div>
      <div>Suite 4, 2071 Pellbrook Rd</div>
      <div>Ferndale Heights 3587</div>
      <div>www.brightharbourwellbeing.com.au</div>
    </address>
    <div class="foot"></div>
    <div class="stripe"></div>
  </section>
</body>
</html>
```